CalmHaven Webpage for Integrative and Holistic Psychiatric Practice

We need a webpage designed for a medical practice that focuses on integrative and holistic psychiatry. We focus on providing care to mothers and families. The name of the company is Calm Haven, incorporated, A Professional Medical Corporation.

We'd like the color palette to be earthy/natural with the same look and feel as our logo that's attached. We're not set on anything, so feel free to have fun with the palette. We just want it to be warm and inviting in particular for Moms!

We'd like to have our logo in the top left with links below it either centered or to the right. We really like websites like http://www.brightmeadowclinic.example/home.html and http://www.tarnwickmindpartners.example/site/ to give you an idea of what we're looking for.

For links, we're looking for the following. Dummy text is fine, we're still getting content together:

* Home
* About Us - this page would have headings for Directions, Staff, Appointment Scheduling
* Services Provided - headings for 8 different services
* Patient Resources - headings for Patient Forms, Fees, Articles
* FAQ
* Contact Us

The webpage will be hosted as an Office 365 Public Website, so feel free to use whatever SharePoint integration you would like, but it's not necessary.

Thank you!

```html
<!DOCTYPE html>
<html lang="en">
<head>
<meta charset="utf-8">
<title>CalmHaven — Psychiatrist for Mothers and Families</title>
<link rel="stylesheet" href="https://fonts.googleapis.com/css2?family=Open+Sans:wdth,wght@75..100,300..800&display=swap">
<style>
:root{
  --green:#2d6406;
  --green-dark:#245104;
  --brown:#5a3310;
  --heading:#666666;
  --text:#5e5e5e;
  --rule:#9a9a9a;
  --white:#ffffff;
  --hero-light:#fbfbfb;
  --hero-mid:#e6e6e6;
}
*{margin:0;padding:0;box-sizing:border-box}
html,body{width:1105px;height:1200px;overflow:hidden;background:var(--white)}
body{position:relative;font-family:"Open Sans",Arial,sans-serif;color:var(--text)}
.abs{position:absolute}

/* header */
.topbar{left:0;top:0;width:1105px;height:49px;background:var(--green)}
.contact-list{right:89px;top:0;height:49px;display:flex;align-items:center;gap:48px;color:var(--white);font-size:14px}
.contact-list span{display:flex;align-items:center;gap:5px}
.contact-list svg{fill:var(--white)}
.navbar{left:0;top:49px;width:1105px;height:31px;border-bottom:1px solid #e2e2e2;background:var(--white)}
.nav{right:91px;top:58px;display:flex;gap:43px;font-size:12px;color:var(--brown)}
.logo-box{left:90px;top:0;width:132px;height:78px;background:var(--white);box-shadow:0 1px 4px rgba(0,0,0,.2);display:flex;align-items:center;justify-content:center;gap:6px}
.logo-dot{width:12px;height:12px;border-radius:50%;background:var(--green)}
.logo-name{font-size:16px;font-weight:600;color:var(--green)}

/* hero */
.hero{left:0;top:80px;width:1105px;height:266px;background:linear-gradient(180deg,var(--hero-light),var(--hero-mid))}
.hero-photo{left:610px;top:80px;width:495px;height:266px;background:linear-gradient(90deg,#e4e6e9 0%,#cfd5dc 35%,#d9b9a0 55%,#c9d2dc 75%,#e9ecef 100%)}
.hero-kicker{left:239px;top:174px;font-weight:300;font-stretch:75%;font-size:30px;color:#555;white-space:nowrap;line-height:1.2}
.hero-title{left:90px;top:208px;font-size:38px;font-weight:700;color:#6a6a6a;letter-spacing:.5px;white-space:nowrap;line-height:1.2}

/* welcome */
.welcome-title{left:0;top:370px;width:1105px;text-align:center;font-size:20px;font-weight:600;color:var(--heading)}
.welcome-text{left:98px;top:402px;width:909px;text-align:center;font-size:11.6px;line-height:19px}

.divider{left:272px;width:621px;height:22px;background:radial-gradient(ellipse at top,rgba(0,0,0,.08),rgba(0,0,0,0) 70%)}

/* services */
.service{top:552px;width:293px}
.section-title{font-size:20px;font-weight:600;color:var(--heading);padding-bottom:2px;border-bottom:1.5px solid var(--rule)}
.service p{margin-top:12px;width:262px;font-size:11.6px;line-height:19px}
.read-more{display:block;margin-top:14px;font-size:10.5px;color:var(--brown);text-transform:uppercase}

/* blog */
.blog{left:90px;top:774px;width:608px}
.post{position:absolute;left:0;width:608px}
.thumb{position:absolute;left:0;top:0;width:81px;height:81px;border-radius:50%;background:radial-gradient(circle at 50% 40%,#d8ad8c,#c9cfd6 60%,#e6e8ea);box-shadow:0 0 0 2px #f0f0f0}
.post p{position:absolute;left:103px;top:3px;width:505px;font-size:11.6px;line-height:19px;text-align:justify}
.post .more{position:absolute;left:103px;top:67px;font-size:10px;color:var(--brown)}
.btn{position:absolute;height:22px;background:var(--green);color:var(--white);font-size:10.5px;display:flex;align-items:center;justify-content:center;border:1px solid var(--green-dark)}

/* testimonials */
.testimonials{left:723px;top:774px;width:292px}
.quote{position:absolute;font-size:32px;font-weight:700;color:#555;line-height:1;font-family:Georgia,serif}
.testimonial{position:absolute;left:0;width:292px;font-size:11.6px;line-height:19px;text-align:justify}
.client{position:absolute;left:-2px;font-size:12px;color:var(--brown)}

/* footer */
.footer{left:0;top:1124px;width:1105px;height:76px;background:var(--green);color:var(--white)}
.copyright{left:90px;top:1155px;font-size:10px;color:var(--white)}
.social{left:478px;top:1145px;display:flex;gap:7px}
.social span{width:32px;height:32px;border-radius:50%;background:var(--white)}
.footer-links{right:91px;top:1155px;font-size:10px;color:var(--white);display:flex;gap:8px}
</style>
</head>
<body>

<header>
  <div class="abs topbar"></div>
  <div class="abs contact-list">
    <span><svg width="14" height="11" viewBox="0 0 14 11"><rect x="0" y="0" width="14" height="11" rx="1"/><path d="M0 1 L7 6 L14 1" stroke="#2d6406" stroke-width="1.4" fill="none"/></svg>info@company.com</span>
    <span><svg width="15" height="13" viewBox="0 0 15 13"><ellipse cx="7.5" cy="5.5" rx="7.5" ry="5.5"/><path d="M2 9 L1 13 L6 10 Z"/></svg>Live Chat</span>
    <span><svg width="12" height="13" viewBox="0 0 12 13"><path d="M2 0 L4.5 0 L5.5 3.5 L4 5 C5 7.5 6.5 9 8 10 L9.5 8.5 L12 9.5 L12 12 C12 12.6 11.5 13 11 13 C5 12.5 0.5 8 0 2 C0 0.8 0.8 0 2 0 Z"/></svg>123-456-7890</span>
  </div>
  <div class="abs navbar"></div>
  <nav class="abs nav">
    <span>Home</span><span>Treatment Philosophy</span><span>Integrative Services</span><span>About</span><span>Faqs</span><span>Blog</span><span>Contact</span>
  </nav>
  <div class="abs logo-box"><span class="logo-dot"></span><span class="logo-name">CalmHaven</span></div>
</header>

<section>
  <div class="abs hero"></div>
  <div class="abs hero-photo" role="img" aria-label="Portrait photo of a smiling mother holding a coffee mug in a bright room"></div>
  <div class="abs hero-kicker">PSYCHIATRIST FOR</div>
  <h1 class="abs hero-title">MOTHERS AND FAMILIES</h1>
</section>

<section>
  <h2 class="abs welcome-title">Welcome to CalmHaven</h2>
  <p class="abs welcome-text">Lorem ipsum dolor sit amet, consectetuer adipiscing elit, sed diam nonummy nibh euismod tincidunt ut laoreet dolore magna aliquam erat volutpat. Ut wisi enim ad minim veniam, Lorem ipsum dolor sit amet, consectetuer adipiscing elit, sed diam nonummy nibh euismod tincidunt ut laoreet dolore magna aliquam erat volutpat. Ut wisi enim ad minim veniam, Lorem ipsum dolor sit amet, consectetuer adipiscing elit, sed diam nonummy nibh euismod tincidunt ut laoreet dolore magna aliquam erat volutpat. Ut wisi enim ad minim veniam, Lorem ipsum dolor sit amet, consectetuer adipiscing elit, sed diam nonummy nibh euismod tincidunt ut laoreet dolore magna aliquam erat volutpat. Ut wisi enim ad minim veniam,</p>
</section>

<div class="abs divider" style="top:530px"></div>

<section>
  <article class="abs service" style="left:90px">
    <h3 class="section-title">Psychiatric Services</h3>
    <p>Lorem ipsum dolor sit amet, consectetuer adipiscing elit, sed diam nonummy nibh euismod tincidunt ut laoreet dolore magna aliquam erat volutpat. Ut wisi enim ad minim veniam,</p>
    <span class="read-more" style="margin-left:3px">Read more</span>
  </article>
  <article class="abs service" style="left:406px">
    <h3 class="section-title">Therapy Services</h3>
    <p>Lorem ipsum dolor sit amet, consectetuer adipiscing elit, sed diam nonummy nibh euismod tincidunt ut laoreet dolore magna aliquam erat volutpat. Ut wisi enim ad minim veniam,</p>
    <span class="read-more">Read more</span>
  </article>
  <article class="abs service" style="left:723px">
    <h3 class="section-title">TMS Therapy</h3>
    <p>Lorem ipsum dolor sit amet, consectetuer adipiscing elit, sed diam nonummy nibh euismod tincidunt ut laoreet dolore magna aliquam erat volutpat. Ut wisi enim ad minim veniam,</p>
    <span class="read-more">Read more</span>
  </article>
</section>

<div class="abs divider" style="top:744px"></div>

<section class="abs blog">
  <h3 class="section-title">Recent Blog Posts</h3>
  <article class="post" style="top:44px">
    <div class="thumb" role="img" aria-label="Blog post photo of a smiling woman"></div>
    <p>Lorem ipsum dolor sit amet, consectetuer adipiscing elit, sed diam nonummy nibh euismod tincidunt ut laoreet dolore magna aliquam erat volutpat. Ut wisi enim ad minim veniam,</p>
    <span class="more">Read more..</span>
  </article>
  <article class="post" style="top:156px">
    <div class="thumb" role="img" aria-label="Blog post photo of a smiling woman"></div>
    <p>Lorem ipsum dolor sit amet, consectetuer adipiscing elit, sed diam nonummy nibh euismod tincidunt ut laoreet dolore magna aliquam erat volutpat. Ut wisi enim ad minim veniam,</p>
    <span class="more">Read more..</span>
  </article>
  <span class="btn" style="left:545px;top:273px;width:63px">See More</span>
</section>

<section class="abs testimonials">
  <h3 class="section-title">Client Testimonials</h3>
  <span class="quote" style="right:0;top:38px">“</span>
  <p class="testimonial" style="top:72px">Lorem ipsum dolor sit amet, consectetuer adipiscing elit, sed diam nonummy nibh euismod tincidunt ut laoreet dolore magna aliquam</p>
  <span class="client" style="top:131px">Client Name / Treatment Name</span>
  <p class="testimonial" style="top:160px">Lorem ipsum dolor sit amet, consectetuer adipiscing elit, sed diam nonummy nibh euismod tincidunt ut laoreet dolore magna aliquam</p>
  <span class="client" style="top:222px">Client Name / Treatment Name</span>
  <span class="quote" style="right:0;top:246px">”</span>
  <span class="btn" style="left:229px;top:273px;width:63px">See More</span>
</section>

<footer>
  <div class="abs footer"></div>
  <span class="abs copyright">Copyright 2014. All rights reserved.</span>
  <div class="abs social" aria-label="Social media links"><span></span><span></span><span></span><span></span></div>
  <div class="abs footer-links"><span>About</span><span>|</span><span>Contact us</span><span>|</span><span>Sitemap</span></div>
</footer>

</body>
</html>
```